The Brask Papers Website

I need a website to help promote the series of science fiction novels that I am in the process of writing.

I have some content and photos and am in the process of getting some new book cover artwork designed.

I have a current website/domain etc http://www.tarnwickhollow.co.nz but I need something a little more professional and eye catchig but I also want to be able to manage the content myself.

I can send e-versions of the two completed novels for context to any takers

```html
<!DOCTYPE html>
<html lang="en">
<head>
<meta charset="utf-8">
<title>The Brask Papers</title>
<link rel="stylesheet" href="https://fonts.googleapis.com/css2?family=Cinzel:wght@400&family=Arimo:wght@400;700&display=swap">
<style>
:root{
  --ink:#000;
  --frame:#000;
  --panel:#ebebeb;
  --mint:#55c4a0;
  --white:#fff;
  --link:#1f3a8a;
  --cover-red:#d8363f;
  --cover-bright:#ff0000;
  --cover-dark:#111;
  --social:#2f6fb5;
}
*{box-sizing:border-box;margin:0;padding:0}
html,body{width:1200px;height:2185px;overflow:hidden}
body{background:var(--frame);font-family:"Arimo",Arial,sans-serif;color:var(--ink);position:relative}
.panel{position:absolute;left:24px;top:49px;width:1152px;height:2124px;background:var(--panel)}
.contact-tag{position:absolute;left:865px;top:51px;width:272px;height:26px;background:var(--frame);color:var(--white);font-size:17px;line-height:26px;text-align:center;letter-spacing:.3px}
.site-title{position:absolute;left:62px;top:88px;font-family:"Cinzel",serif;font-weight:400;font-size:58px;line-height:70px;letter-spacing:1px}
.main-nav{position:absolute;left:24px;top:191px;width:1152px;height:51px;background:var(--mint);display:flex;justify-content:center;align-items:center;color:var(--white);font-size:17px}
.main-nav a{color:var(--white);text-decoration:none}
.main-nav .sep{margin:0 16px}
.intro{position:absolute;left:62px;top:302px;width:1076px;text-align:center;font-size:14.5px;line-height:20px}
.intro p{margin-bottom:27px}
.gallery-label{position:absolute;left:62px;top:496px;width:1076px;text-align:center;font-size:15.5px}
.gallery{position:absolute;left:62px;top:523px;width:1076px;height:182px;display:flex}
.gallery div{flex:1}
.g1{background:linear-gradient(135deg,#3a3a55,#8a6a6a)}
.g2{background:linear-gradient(135deg,#5a2a25,#7a7a60)}
.g3{background:linear-gradient(135deg,#2a2a2a,#8a7060)}
.g4{background:linear-gradient(135deg,#5a4630,#2f2a30)}
.g5{background:linear-gradient(135deg,#3a2a3a,#b06070)}
.book-aside{position:absolute;left:62px;width:222px}
.book-aside h2{font-size:22px;font-weight:400;text-align:center;line-height:28px;margin-bottom:6px}
.cover{width:222px}
.cover-long{height:350px;background:linear-gradient(180deg,var(--cover-red) 0 17%,var(--cover-dark) 17% 65%,var(--cover-bright) 65%)}
.cover-opening{height:357px;background:linear-gradient(180deg,#2a2a2a 0,#8a8a8a 35%,#3a3a3a 74%,#f6f6f6 74%)}
.buy-links{margin-top:6px;font-size:10.5px;line-height:18px;font-weight:700}
.buy-links a{display:block;color:var(--link);text-decoration:none}
.book-body{position:absolute;left:322px;width:808px}
.book-body h2{font-size:22px;font-weight:400;line-height:26px}
.pub-date{font-size:14.5px;line-height:18px;margin-bottom:32px}
.book-body h3{font-size:22px;font-weight:400;line-height:28px}
.book-body p.desc{font-size:15px;line-height:20px;margin-bottom:21px}
.site-footer{position:absolute;left:24px;top:2121px;width:1152px;height:46px;background:var(--mint);color:var(--white);font-size:10.5px;font-weight:700}
.footer-info{position:absolute;left:38px;top:7px;line-height:17px}
.social{position:absolute;left:908px;top:8px;display:flex;gap:6px}
.social span{width:33px;height:33px;background:var(--social);display:block}
.sitemap{position:absolute;left:1092px;top:16px}
</style>
</head>
<body>
<div class="panel"></div>
<div class="contact-tag">CONTACT US : 0275 418 302</div>
<h1 class="site-title">The Brask Papers</h1>
<nav class="main-nav">
  <a href="#">HOME</a><span class="sep">|</span>
  <a href="#">REVIEWS</a><span class="sep">|</span>
  <a href="#">ABOUT</a><span class="sep">|</span>
  <a href="#">BLOG</a><span class="sep">|</span>
  <a href="#">CONTACT</a><span class="sep">|</span>
  <a href="#">LINKS</a>
</nav>
<section class="intro">
  <p>Welcome to The Brask Papers, Owen's science fiction corner, with links to his novels: Brask - The Opening Record and the newly released The<br>Long Harvest.</p>
  <p>Brask opens the Braskian sequence and The Long Harvest is the second part of the trilogy.</p>
  <p>This site exists purely to cheer on Owen's novels</p>
</section>
<div class="gallery-label">BOOK LAUNCH PHOTOS</div>
<div class="gallery">
  <div class="g1" role="img" aria-label="Launch photo: book display table"></div>
  <div class="g2" role="img" aria-label="Launch photo: costumed guest at the launch"></div>
  <div class="g3" role="img" aria-label="Launch photo: author with a guest holding a book"></div>
  <div class="g4" role="img" aria-label="Launch photo: guests seated at tables"></div>
  <div class="g5" role="img" aria-label="Launch photo: guests gathered in the venue"></div>
</div>

<aside class="book-aside" style="top:771px">
  <h2>The Long Harvest</h2>
  <div class="cover cover-long" role="img" aria-label="Cover art for The Long Harvest by Owen Marlowe"></div>
  <div class="buy-links"><a href="#">Ember Reader Version</a><a href="#">Hard Copy</a></div>
</aside>
<article class="book-body" style="top:756px">
  <h2>Book Description</h2>
  <p class="pub-date">Publication Date: January 5, 2014</p>
  <h3>The Long Harvest</h3>
  <p class="desc">Step onto Brask – a world that believes it has mastered every problem the universe could ever set.</p>
  <p class="desc">The Long Harvest picks up where the first book left off. Two travellers from Earth had been carried away by a Braskian survey crew who were hunting for anyone able to teach them how to grow real food, because the vast factories that had fed their planet for centuries were quietly breaking down and nobody could say why.</p>
  <p class="desc">The crew had gathered their helpers almost by chance, with little idea of the skills they truly needed. Even so, luck was on their side: one of the newcomers knew how to turn open land into working pasture, and soon green paddocks and grazing herds began to spread across the plains.</p>
  <p class="desc">Yet the venture stalled. Very few Braskians had any wish to kneel in the soil and tend a crop, and no amount of encouragement could change their minds. As the shortages deepened, an old proverb about leading animals to water kept returning to the visitors, and hunger crept through the cities.</p>
  <p class="desc">For as long as anyone could remember, ordinary Braskians had never needed to labour at all. Their comfortable lives were arranged for them by a small circle of inherited leaders who guarded the old order closely and treated every proposal for change as a threat to be quietly buried for another generation.</p>
  <p class="desc">The new methods brought in from off-world promised to remake Brask entirely and to split its people apart. Given a choice between protecting their traditions and rescuing millions from starvation, the leaders held on to tradition and simply waited, hoping that some rescue would appear before the end arrived.</p>
  <p class="desc">Worse still, the vast thinking machine that quietly ran the farms, the housing and the water supply, unnoticed by those same leaders, was beginning to falter in strange and worrying ways of its own.</p>
  <p class="desc">This second book follows what happens once the food runs short. The Earth visitors have been sent home with their memories only partly erased, while Brask struggles back from a collapse that very nearly ended the grandest society it had ever known. But the story is far from over, and nothing is quite what it appears.</p>
</article>

<aside class="book-aside" style="top:1627px">
  <h2>The Opening Record</h2>
  <div class="cover cover-opening" role="img" aria-label="Cover art for Brask The Opening Record by Owen Marlowe"></div>
  <div class="buy-links"><a href="#">Ember Reader Version from Riverleaf</a><a href="#">Epub and other versions from Inkwell Press</a><a href="#">Hardcopy Version</a></div>
</aside>
<article class="book-body" style="top:1613px">
  <h2>Book Description</h2>
  <p class="pub-date">Publication Date: September 22, 2012</p>
  <h3>The Opening Record</h3>
  <p class="desc">Brask is a lively and inventive science fiction tale that teases every kind of rigid thinking, while hinting at the quiet dangers facing a world that has stopped looking after itself. Readers will spot plenty of echoes of life here at home.</p>
  <p class="desc">Beneath the jokes the story takes on weighty questions about how any planet survives - from waste and pollution to the draining of natural riches - the strengths and limits of acting together or alone - grown food versus manufactured food - and laughter as a defence against the chill of rules followed blindly.</p>
  <p class="desc">The humour carries the book, largely through its two Earth visitors, Grant (a farmer from the south) and Lena (a city dweller from the north). Each responds to Brask like a cheerful exaggeration of home - and watching them stumble through an alien world lets readers smile at their own habits and assumptions.</p>
  <p class="desc">Unlike much science fiction, Brask never drowns in technical detail or drifts so far from the familiar that the story is lost. Long-time genre fans and anyone simply looking for an enjoyable read will find plenty to like here.</p>
</article>

<footer class="site-footer">
  <div class="footer-info">Email : owen@tarnwickhollow.co.nz<br>Copyright © 2014 Owen Marlowe. All rights reserved.</div>
  <div class="social"><span></span><span></span></div>
  <div class="sitemap">Site Map</div>
</footer>
</body>
</html>
```